The Pemberly Nine Modes of Inventive Spark Graphics

DESIGN ELEMENT 1: The Pemberly Nine Modes of Inventive Spark Wheel/Circle
A circular diagram showing all 12 types organized by their three domains.
I attached what I have so far, I created this in PPT. It uses some of the elements you have already created for me like the colors and fonts.
I've also attached a representation of the 3 Domains (Relational, Analytical and Functional)
DESIGN ELEMENT 2: The Nine Personas of Inventive Spark (Human Representations)
The Connector, The Cultivator, The Healer, The Teacher, The Communicator, The Scientist, The Strategist, The Synthesizer, The Artist, The Builder, The Designer, The Organizer.
Each of the 12 types represented as a human figure.
Style options to consider:
• Silhouettes — Clean, simple, universal (gender-neutral, racially ambiguous). Each silhouette could hold or interact with a symbol of their type.
• Or Illustrated figures — More personality, could show action/posture that reflects the type (e.g., Connector introducing people reaching out hands, Builder holding tools, Artist painting, Strategist looking toward horizon)
• Abstract/geometric figures — Modern, stylized human forms with symbolic elements
Key considerations:
• Diversity & inclusivity — If using detailed illustrations, represent diverse ages, genders, races, body types. If using silhouettes, keep them universal.
• Action/posture — Each figure should be doing something that reflects their type (connecting, building, healing, teaching, etc.)
• Consistency — All 12 should feel like they belong to the same visual family while being distinct from each other.
An idea: Silhouettes might be strongest—they're inclusive, timeless, and let the reader project themselves into the type. Each silhouette could be shown with one signature object or in one signature pose. But I’m open to other ideas.
TONE & FEEL
• Empowering — "You ARE creative"
• Inclusive — For corporations, classrooms, faith congregations, clinics, communities
• Warm but credible — Grounded in psychology research, but accessible and human
• Revolutionary — "The Inventive Spark Uprising"
The design should feel:
• Modern but not cold
• Professional but not too corporate
• Hopeful, energizing, inviting
• Sophisticated enough for business readers, warm enough for everyone else

```html
<!DOCTYPE html>
<html lang="en">
<head>
<meta charset="utf-8">
<title>The Pemberly Nine Modes of Inventive Spark</title>
<link rel="stylesheet" href="https://fonts.googleapis.com/css2?family=Poppins:wght@300;500&family=Yellowtail&display=swap">
<style>
  :root {
    --frame: #7f7fac;
    --paper: #ffffff;
    --ink: #2b2b2b;
    --leader: #9a9a9a;
    --functional: #2e3287;
    --relational: #e92a7a;
    --analytical: #f39025;
    --builder: #585b9c;
    --designer: #7f7fac;
    --organizer: #a5a5bd;
    --artist: #33358a;
    --connector: #e92a7a;
    --cultivator: #ef5795;
    --healer: #f589b6;
    --teacher: #fdb3d2;
    --synthesizer: #f39025;
    --strategist: #f5a64f;
    --scientist: #fbbd7b;
    --communicator: #fdd4a7;
  }
  html, body {
    margin: 0;
    padding: 0;
    width: 1200px;
    height: 905px;
    overflow: hidden;
    background: var(--paper);
  }
  .canvas {
    position: relative;
    width: 1200px;
    height: 905px;
    box-sizing: border-box;
    border: 10px solid var(--frame);
    background: var(--paper);
  }
  .wheel-art {
    position: absolute;
    left: -10px;
    top: -10px;
    width: 1200px;
    height: 905px;
  }
  .type-label {
    font-family: "Poppins", sans-serif;
    font-weight: 500;
    font-size: 16px;
    fill: var(--ink);
  }
  .domain-label {
    font-family: "Poppins", sans-serif;
    font-weight: 500;
    font-size: 20.5px;
    fill: var(--ink);
  }
  .hub-kicker {
    font-family: "Poppins", sans-serif;
    font-weight: 300;
    font-size: 15.5px;
    fill: var(--ink);
  }
  .hub-title {
    font-family: "Yellowtail", cursive;
    font-size: 37px;
    fill: var(--ink);
  }
  .leader { fill: none; stroke: var(--leader); stroke-width: 1.2; }
  .domain-arc { fill: none; stroke-width: 4.5; }
  .wedge { stroke: var(--paper); stroke-width: 10; stroke-linejoin: miter; }
  .icon { fill: none; stroke: var(--paper); stroke-width: 4; stroke-linecap: round; stroke-linejoin: round; }
  .icon-fill { fill: var(--paper); stroke: none; }
</style>
</head>
<body>
<div class="canvas">
  <svg class="wheel-art" viewBox="0 0 1200 905" xmlns="http://www.w3.org/2000/svg">
    <defs>
      <path id="wedge-shape" d="M0,-126 L0,-269 A269,269 0 0 1 134.5,-232.96 L63,-109.12 A126,126 0 0 0 0,-126 Z"/>
    </defs>

    <!-- leader lines -->
    <polyline class="leader" points="378,135 570,135 600,187"/>
    <polyline class="leader" points="237,766 392,766 436,723"/>
    <polyline class="leader" points="966,766 809,766 766,723"/>

    <g transform="translate(600 481)">
      <!-- domain arcs -->
      <path class="domain-arc" stroke="var(--functional)" d="M-239,-155.2 A285,285 0 0 1 239,-155.2"/>
      <path class="domain-arc" stroke="var(--relational)" d="M256.2,-124.9 A285,285 0 0 1 17.4,284.5"/>
      <path class="domain-arc" stroke="var(--analytical)" d="M-17.4,284.5 A285,285 0 0 1 -256.2,-124.9"/>

      <!-- wedges, clockwise from top -->
      <use class="wedge" href="#wedge-shape" fill="var(--designer)" transform="rotate(0)"/>
      <use class="wedge" href="#wedge-shape" fill="var(--organizer)" transform="rotate(30)"/>
      <use class="wedge" href="#wedge-shape" fill="var(--connector)" transform="rotate(60)"/>
      <use class="wedge" href="#wedge-shape" fill="var(--cultivator)" transform="rotate(90)"/>
      <use class="wedge" href="#wedge-shape" fill="var(--healer)" transform="rotate(120)"/>
      <use class="wedge" href="#wedge-shape" fill="var(--teacher)" transform="rotate(150)"/>
      <use class="wedge" href="#wedge-shape" fill="var(--synthesizer)" transform="rotate(180)"/>
      <use class="wedge" href="#wedge-shape" fill="var(--strategist)" transform="rotate(210)"/>
      <use class="wedge" href="#wedge-shape" fill="var(--scientist)" transform="rotate(240)"/>
      <use class="wedge" href="#wedge-shape" fill="var(--communicator)" transform="rotate(270)"/>
      <use class="wedge" href="#wedge-shape" fill="var(--artist)" transform="rotate(300)"/>
      <use class="wedge" href="#wedge-shape" fill="var(--builder)" transform="rotate(330)"/>

      <!-- designer: brush -->
      <g class="icon" transform="translate(51 -190) rotate(18)">
        <line x1="0" y1="-38" x2="0" y2="4" stroke-width="6"/>
        <line x1="-5" y1="10" x2="5" y2="10"/>
        <line x1="-5" y1="16" x2="5" y2="16"/>
        <path class="icon-fill" d="M-6,20 L6,20 L4,32 Q0,42 -8,40 Q-3,34 -6,20 Z"/>
      </g>

      <!-- organizer: checklist -->
      <g class="icon" transform="translate(139 -139)">
        <polyline points="-26,-18 -23,-14 -19,-22" stroke-width="3"/>
        <polyline points="-26,-3 -23,1 -19,-7" stroke-width="3"/>
        <polyline points="-26,12 -23,16 -19,8" stroke-width="3"/>
        <line x1="-12" y1="-15" x2="24" y2="-15"/>
        <line x1="-12" y1="0" x2="24" y2="0"/>
        <line x1="-12" y1="15" x2="24" y2="15"/>
      </g>

      <!-- connector: branching plug -->
      <g class="icon" transform="translate(190 -51)">
        <line x1="0" y1="-24" x2="0" y2="22"/>
        <path class="icon-fill" d="M0,-34 L-7,-24 L7,-24 Z"/>
        <path d="M-14,-8 L-14,2 L0,12"/>
        <circle cx="-14" cy="-12" r="4"/>
        <path d="M14,-12 L14,-2 L0,8"/>
        <rect class="icon-fill" x="9" y="-20" width="10" height="9"/>
        <circle class="icon-fill" cx="0" cy="27" r="6"/>
      </g>

      <!-- cultivator: sickle -->
      <g class="icon" transform="translate(190 51)">
        <path d="M4,-30 Q34,-6 12,22 Q0,30 -14,24"/>
        <path d="M8,-26 Q24,-6 10,16" stroke-width="2.5"/>
        <line x1="-14" y1="24" x2="-30" y2="40" stroke-width="5"/>
      </g>

      <!-- healer: bandage -->
      <g transform="translate(139 139) rotate(-40)">
        <rect class="icon" x="-30" y="-12" width="60" height="24" rx="12"/>
        <rect class="icon-fill" x="-9" y="-8" width="18" height="16" rx="2"/>
        <circle class="icon-fill" cx="-20" cy="-4" r="1.8"/>
        <circle class="icon-fill" cx="-20" cy="4" r="1.8"/>
        <circle class="icon-fill" cx="20" cy="-4" r="1.8"/>
        <circle class="icon-fill" cx="20" cy="4" r="1.8"/>
      </g>

      <!-- teacher: board -->
      <g class="icon" transform="translate(51 190)">
        <rect x="-24" y="-28" width="48" height="36" stroke-width="3"/>
        <line x1="-28" y1="12" x2="28" y2="12" stroke-width="3"/>
        <line x1="-16" y1="12" x2="-22" y2="32" stroke-width="3"/>
        <line x1="16" y1="12" x2="22" y2="32" stroke-width="3"/>
        <line x1="-14" y1="-14" x2="10" y2="-14" stroke-width="2.5"/>
        <line x1="-14" y1="-4" x2="4" y2="-4" stroke-width="2.5"/>
      </g>

      <!-- synthesizer: merging arrows -->
      <g class="icon" transform="translate(-51 190)">
        <line x1="8" y1="-30" x2="8" y2="-6"/>
        <line x1="-4" y1="-18" x2="24" y2="-18"/>
        <polyline points="8,-6 -26,28"/>
        <polyline points="-26,14 -26,28 -12,28"/>
        <polyline points="-4,-18 -30,8"/>
        <polyline points="-30,-4 -30,8 -18,8"/>
      </g>

      <!-- strategist: play diagram -->
      <g class="icon" transform="translate(-139 139)" stroke-width="3">
        <circle cx="-18" cy="-18" r="5"/>
        <circle cx="-18" cy="20" r="5"/>
        <circle cx="20" cy="20" r="5"/>
        <line x1="15" y1="-23" x2="25" y2="-13"/>
        <line x1="25" y1="-23" x2="15" y2="-13"/>
        <line x1="-12" y1="14" x2="14" y2="-12" stroke-dasharray="1 5"/>
      </g>

      <!-- scientist: atom -->
      <g class="icon" transform="translate(-190 51)" stroke-width="3">
        <ellipse cx="0" cy="0" rx="33" ry="12"/>
        <ellipse cx="0" cy="0" rx="33" ry="12" transform="rotate(60)"/>
        <ellipse cx="0" cy="0" rx="33" ry="12" transform="rotate(-60)"/>
        <circle class="icon-fill" cx="0" cy="0" r="6"/>
      </g>

      <!-- communicator: speech bubble -->
      <g class="icon" transform="translate(-190 -51)" stroke-width="3.5">
        <path d="M-20,18 A26,24 0 1 1 -8,23 L-26,30 Z"/>
        <line x1="-12" y1="-6" x2="12" y2="-6"/>
        <line x1="-12" y1="4" x2="12" y2="4"/>
      </g>

      <!-- artist: palette -->
      <g transform="translate(-142 -145)">
        <path class="icon-fill" d="M2,-30 C28,-30 38,-12 30,-6 C24,-2 10,-6 10,6 C10,16 22,20 16,26 C8,34 -22,32 -28,12 C-34,-10 -20,-30 2,-30 Z"/>
        <circle cx="-16" cy="-12" r="4.5" fill="none" stroke="var(--artist)" stroke-width="2.5"/>
        <circle cx="-2" cy="-20" r="4.5" fill="none" stroke="var(--artist)" stroke-width="2.5"/>
        <circle cx="14" cy="-18" r="4.5" fill="none" stroke="var(--artist)" stroke-width="2.5"/>
        <circle cx="-16" cy="4" r="4.5" fill="none" stroke="var(--artist)" stroke-width="2.5"/>
        <circle cx="0" cy="18" r="7" fill="var(--artist)"/>
      </g>

      <!-- builder: tools -->
      <g class="icon" transform="translate(-51 -190)">
        <line x1="-22" y1="22" x2="8" y2="-8" stroke-width="6"/>
        <circle cx="-22" cy="22" r="3" class="icon-fill"/>
        <path d="M8,-8 A12,12 0 1 0 18,-22" stroke-width="5"/>
        <line x1="-22" y1="-24" x2="-12" y2="-14" stroke-width="4"/>
        <line x1="-12" y1="-14" x2="22" y2="20" stroke-width="6"/>
      </g>

      <!-- hub -->
      <text class="hub-kicker" x="0" y="-20" text-anchor="middle">The PEMBERLY Nine Modes of</text>
      <text class="hub-title" x="0" y="24" text-anchor="middle">Inventive Spark</text>
    </g>

    <!-- type labels -->
    <text class="type-label" x="433" y="193">The Builder</text>
    <text class="type-label" x="693" y="199">The Designer</text>
    <text class="type-label" x="374" y="269" text-anchor="end">The Artist</text>
    <text class="type-label" x="808" y="269">The Organizer</text>
    <text class="type-label" x="311" y="428" text-anchor="end">The Communicator</text>
    <text class="type-label" x="882" y="428">The Connector</text>
    <text class="type-label" x="311" y="566" text-anchor="end">The Scientist</text>
    <text class="type-label" x="885" y="566">The Cultivator</text>
    <text class="type-label" x="296" y="709">The Strategist</text>
    <text class="type-label" x="816" y="709">The Healer</text>
    <text class="type-label" x="595" y="794" text-anchor="end">The Synthesizer</text>
    <text class="type-label" x="636" y="794">The Teacher</text>

    <!-- domain labels -->
    <text class="domain-label" x="126" y="143">Functional Genius Domain</text>
    <text class="domain-label" x="175" y="771" text-anchor="middle">Analytical</text>
    <text class="domain-label" x="175" y="795" text-anchor="middle">Genius Domain</text>
    <text class="domain-label" x="1028" y="771" text-anchor="middle">Relational</text>
    <text class="domain-label" x="1028" y="795" text-anchor="middle">Genius Domain</text>
  </svg>
</div>
</body>
</html>
```